Brisco & Tennant Price List for Dealers

Looking for a 4 pages total including front and back of catalog. Looking for a PDF that we can upload to a printer for production. Full color, professional looking. We have uploaded our current price list, just need to have it look a little more updated. See our website BriscoandTennant.com for more info on us, see our competitor DorvinandHale.com, see our vendors Trelvane.com, Morbrix.com, Quenlar.com, Dwip.com

Target Market(s)

automotive dealers, selling aftermarket products. Sunroofs, leather interiors, seat heaters, convertible top repairs, interior work see BriscoandTennant.com for info, also see our competitors dorvinandhale.com . See our vendors Trelvane.com, Morbrix.com, Quenlar.com, Dwip.com

Industry/Entity Type

Automotive

Font styles to use
Serif

Colors

Designer to choose colors to be used in the design.

Requirements
Must have
• Logo, phone number, fax number, web address and email address which is INFO@BRISCOANDTENNANT.COM
Nice to have
• just looking for a nice, professional price list/catalog to hand out at auto dealers who sell our product.

```html
<!DOCTYPE html>
<html lang="en">
<head>
<meta charset="utf-8">
<title>Brisco &amp; Tennant Dealer Price List</title>
<link href="https://fonts.googleapis.com/css2?family=Audiowide&family=Source+Sans+3:ital,wght@0,400;0,600;0,700;1,700&display=swap" rel="stylesheet">
<style>
:root{
  --blue:#0a2f8f;
  --blue-dark:#062475;
  --ink:#2a2a2a;
  --paper:#ffffff;
  --spine:#d9d9d9;
  --bg:#eeeeee;
}
*{margin:0;padding:0;box-sizing:border-box}
html,body{width:1200px;height:1200px;overflow:hidden;background:var(--bg)}
body{font-family:"Source Sans 3",sans-serif;color:var(--ink)}
.spread{position:absolute;left:14px;top:147px;width:1172px;height:906px;background:var(--paper);box-shadow:0 6px 20px rgba(0,0,0,.18)}
.page-right{position:absolute;left:586px;top:0;width:586px;height:906px;background:linear-gradient(90deg,var(--spine) 0,#f1f1f1 120px,#fff 320px)}
.abs{position:absolute}
.band{position:absolute;left:0;top:0;width:1172px;height:906px}
.tab-title{position:absolute;font-family:"Audiowide",sans-serif;color:#fff;font-size:21px;letter-spacing:.5px;line-height:1}
.photo{position:absolute;width:256px;height:120px;border-radius:18px}
.photo-convertible{background:linear-gradient(160deg,#5d6b55 0,#8a8f84 35%,#b3202a 60%,#7a1118 100%)}
.photo-leather{background:linear-gradient(150deg,#3a4a63 0,#1d2a40 55%,#c9d2de 100%)}
.photo-dash{background:linear-gradient(135deg,#2b2b2b 0,#6b6b6b 45%,#c8c8c8 70%,#e9d9cf 100%)}
.seat-art{position:absolute;left:355px;top:672px;width:160px;height:234px;border-radius:40px 40px 10px 10px;background:linear-gradient(180deg,#4a4a4a 0,#9a9a9a 40%,#d8d8d8 65%,#3a3a3a 100%)}
.tagline{position:absolute;left:42px;top:245px;color:var(--blue);font-size:17px;line-height:19.7px}
.tagline b{font-weight:700;font-style:italic}
.promo{position:absolute;left:629px;color:var(--blue);font-size:17px;line-height:19.7px}
.col{position:absolute;font-size:12px;line-height:13.4px}
.col h3{color:var(--blue);font-size:12px;font-weight:700;letter-spacing:.2px;line-height:13px;margin-bottom:14px}
.col h4{font-size:12px;font-weight:700}
.col b{font-weight:700}
.blk{margin-bottom:13px}
.row{display:flex;justify-content:space-between}
ul{list-style:none}
li{padding-left:10px;position:relative}
li::before{content:"•";position:absolute;left:0}
.opt-head{color:var(--blue);font-weight:700}
</style>
</head>
<body>
<div class="spread">
  <div class="page-right"></div>

  <svg class="band" viewBox="0 0 1172 906" aria-hidden="true">
    <g fill="var(--blue)">
      <rect x="0" y="42" width="545" height="3"/>
      <path d="M192 43 H543 L535 80 Q534 85 528 85 H207 Q198 85 197 76 Z"/>
      <rect x="0" y="391" width="545" height="3"/>
      <path d="M192 392 H543 L535 429 Q534 434 528 434 H207 Q198 434 197 425 Z"/>
      <path d="M641 43 H980 L972 80 Q971 85 965 85 H636 Q629 85 629 78 L633 52 Q635 43 641 43 Z"/>
      <rect x="975" y="42" width="197" height="3"/>
      <path d="M641 432 H980 L972 469 Q971 474 965 474 H636 Q629 474 629 467 L633 441 Q635 432 641 432 Z"/>
      <rect x="975" y="431" width="197" height="3"/>
    </g>
  </svg>

  <div class="tab-title" style="left:229px;top:55px">Sunroofs</div>
  <div class="tab-title" style="left:229px;top:403px">Leather Interiors</div>
  <div class="tab-title" style="left:668px;top:52px">Safety &amp; Convenience</div>
  <div class="tab-title" style="left:668px;top:442px">Mobile Video</div>

  <div class="photo photo-convertible" style="left:43px;top:106px" role="img" aria-label="Couple driving a red convertible on a country road"></div>
  <div class="photo photo-leather" style="left:43px;top:455px" role="img" aria-label="Hand wiping a dark leather car seat with a cloth"></div>
  <div class="seat-art" role="img" aria-label="Two-tone grey leather car seat"></div>
  <div class="photo photo-dash" style="left:629px;top:106px" role="img" aria-label="Finger touching a dashboard navigation screen"></div>
  <div class="photo photo-dash" style="left:629px;top:495px" role="img" aria-label="Finger touching a dashboard video screen"></div>

  <p class="tagline"><b>Don’t go to just anyone!</b><br>We have been installing sunroofs<br>Since 1973- Trust the Pros.<br>All sunroofs come with a limited<br>lifetime warranty.</p>

  <div class="col" style="left:341px;top:104px;width:200px">
    <h3>FULL FEATURE AUTO-CLOSE<br>SUNROOFS</h3>
    <div class="blk">
      <div style="display:flex"><span style="width:100px">All Cars</span><b>$995.00</b></div>
      <div style="display:flex"><span style="width:100px">Vans and SUV’s</span><b>$1295.00</b></div>
    </div>
    <div class="blk">
      <h4>Additional</h4>
      <ul>
        <li>Rerouting Overhead Air Vents add<br><b>$100.00</b></li>
        <li>Vehicles with ridges on roof add<br><b>$100.00</b></li>
        <li>Overhead Consoles add<br><b>$50.00</b></li>
      </ul>
    </div>
    <div class="blk">Spoiler Sunroofs-External<br>Sliding Glass<br><b>$895.00</b></div>
    <div>Spoiler Sunroofs-With Auto-Close<br><b>$995.00</b></div>
  </div>

  <div class="col" style="left:42px;top:594px;width:260px">
    <h3>LEATHER PACKAGES</h3>
    <div class="blk" style="line-height:15px">
      <div class="row"><span>Two Row Seating</span><b>$&nbsp;&nbsp;945.00</b></div>
      <div class="row"><span>Three Row Seating</span><b>$1345.00</b></div>
    </div>
    <div style="line-height:15px">
      <h4>Options</h4>
      <div class="row"><span>Two Tone Color Combos</span><span>add <b>$100.00</b></span></div>
      <div class="row"><span>Exotics (Inserts)</span><span>add <b>$150.00</b></span></div>
      <div class="row"><span>Embroidery/Logo</span><span>add <b>$100.00</b></span></div>
      <div class="row"><span>Perforation</span><span>add <b>$&nbsp;&nbsp;50.00</b></span></div>
      <div class="row"><span>Overnight Shipping on 2 Row add</span><b>$&nbsp;&nbsp;75.00</b></div>
      <div class="row"><span>Overnight Shipping on 3 Row add</span><b>$100.00</b></div>
    </div>
  </div>

  <div class="col" style="left:341px;top:454px;width:200px">
    <h3>SEAT HEATING &amp; POWER LUMBAR</h3>
    <div class="blk">
      <h4>Seat Heaters</h4>
      With Leather Package (For Pair)<br><b>$295.00</b><br>
      Without Leather Package (Each)<br><b>$295.00</b>
    </div>
    <div>
      <h4>Power Lumbar</h4>
      With Leather Package (For Pair)<br><b>$395.00</b><br>
      Without Leather Package (Each)<br><b>$425.00</b><br>
      Seat Heater and Cooling System<br>Each Seat<br><b>$595.00</b>
    </div>
  </div>

  <div class="col" style="left:629px;top:245px;width:260px">
    <h3 style="margin-bottom:17px">NAVIGATION SYSTEMS</h3>
    <div class="blk" style="line-height:14.6px">
      <div class="row"><span>Factory Radio Integration</span><b>From $1195.00</b></div>
      <div class="row"><span>Factory Look-A-like Navigation</span><b>From $1295.00</b></div>
      <div class="row"><span>Halvern Navigation System</span><b>$1295.00</b></div>
      <div class="row"><span>Corvane System</span><b>$1595.00</b></div>
    </div>
    <div>* Call For Pricing If Vehicle Has Steering<br>&nbsp;&nbsp;Wheel Controls/Amplifier</div>
  </div>

  <div class="col" style="left:927px;top:104px;width:204px">
    <h3>REAR SENSING SYSTEMS</h3>
    <div class="blk row"><span>Blind Spot Sensors</span><b>$695.00</b></div>
    <div class="blk">Backup Sensors
      <div class="row"><span>2 Sensor Set</span><b>$350.00</b></div>
      <div class="row"><span>3 Sensor Set</span><b>$500.00</b></div>
    </div>
    <div class="blk row"><span>Rear Camera Video System</span><b>$795.00</b></div>
    <div class="blk">Rear Camera With<div class="row"><span>Navigation Installation</span><b>$395.00</b></div></div>
    <div class="blk">Rear Camera<div class="row"><span>Into Auto-Dimming Mirror</span><b>$795.00*</b></div></div>
    <div class="blk">* Optional Temperature/Compass/<br>&nbsp;&nbsp;RoadLink Call For Pricing</div>
    <div><h4>Advanced Rear View Mirror</h4>Auto-Dimming, Compass,<br>Outside Temperature<br><b>$695.00</b></div>
  </div>

  <p class="promo" style="top:634px">All Units Include Monitor,<br>Wireless Remote &amp; 2 Wireless<br>Headphones.</p>
  <p class="promo" style="top:712px">Audio Comes Through Vehicle’s<br>Stereo System.</p>
  <p class="promo" style="top:771px">All-n-One Overhead<br>Flip Down Monitor W/DVD<br><b style="font-weight:700">$795.00</b></p>

  <div class="col" style="left:927px;top:493px;width:215px">
    <h3>HEADREST DVD SYSTEMS</h3>
    <div class="blk">7” Headrest Monitors –<br>Black, Grey or Tan Leather<br><b>$995 to $1195.00</b></div>
    <div class="blk">9” Headrest Monitors –<br>Black, Grey or Tan Leather<br><b>$1195 to $1395.00</b></div>
    <div class="blk">Factory Match Cloth or<br>Leather DVD Headrest System<br><b>$1595.00</b></div>
    <div class="blk">SmartVista Factory Match Headrests<br>W/Removable Tablets<br>8GB&nbsp;&nbsp;&nbsp;<b>$1495.00</b><br>16GB&nbsp;&nbsp;<b>$1695.00</b><br>32GB&nbsp;&nbsp;<b>$1795.00</b></div>
    <div>
      <div class="opt-head">Options</div>
      <ul>
        <li>Extra Headphone <b>$75.00</b></li>
        <li>Power Inverter <b>Call For Pricing</b></li>
        <li>Headrest Input Into Navigation/<br>Radio Screen <b>Call For Pricing</b></li>
      </ul>
    </div>
  </div>
</div>
</body>
</html>
```